Email Signatures

I would like to create a new email signature for my team. The design will be the same for everyone, with only individual details such as name and email changing. You can also see our brand style on our website. https://www.tlmbespokehomes.com.au/

Target Market(s)

Clients for new builds or renovations

Industry/Entity Type

Construction

Colors

Designer to choose colors to be used in the design.

```html
<!DOCTYPE html>
<html lang="en">
<head>
<meta charset="utf-8">
<title>TLM Bespoke Homes – Email Signature</title>
<link href="https://fonts.googleapis.com/css2?family=Montserrat:wght@400;500;600&display=swap" rel="stylesheet">
<style>
  :root {
    --page-bg: #d4d4d4;
    --panel-bg: #151515;
    --brand-green: #0f9447;
    --text-light: #f4f4f4;
    --divider: #5a5a5a;
  }
  html, body {
    margin: 0;
    padding: 0;
    width: 1200px;
    height: 1200px;
    overflow: hidden;
    background: var(--page-bg);
    font-family: "Montserrat", Arial, sans-serif;
  }
  .signature {
    position: absolute;
    left: 58px;
    top: 453px;
    width: 1100px;
    height: 302px;
    background: var(--panel-bg);
    box-shadow: 0 4px 10px rgba(0,0,0,0.18);
  }
  .signature__band {
    position: absolute;
    left: 0;
    bottom: 0;
    width: 100%;
    height: 16px;
    background: var(--brand-green);
  }
  .person__name {
    position: absolute;
    left: 42px;
    top: 44px;
    margin: 0;
    font-size: 43px;
    font-weight: 600;
    letter-spacing: 2px;
    line-height: 1;
    color: var(--brand-green);
  }
  .person__role {
    position: absolute;
    left: 42px;
    top: 84px;
    margin: 0;
    font-size: 25px;
    font-weight: 400;
    letter-spacing: 0.5px;
    line-height: 1.2;
    color: var(--text-light);
  }
  .person__rule {
    position: absolute;
    left: 46px;
    top: 120px;
    width: 54px;
    height: 2px;
    background: var(--brand-green);
  }
  .contact-list {
    position: absolute;
    left: 44px;
    top: 136px;
    margin: 0;
    padding: 0;
    list-style: none;
  }
  .contact-list__item {
    display: flex;
    align-items: center;
    height: 38px;
    font-size: 25px;
    font-weight: 400;
    color: var(--text-light);
  }
  .contact-list__icon {
    width: 26px;
    height: 26px;
    margin-right: 10px;
    flex: none;
  }
  .signature__divider {
    position: absolute;
    left: 569px;
    top: 76px;
    width: 1px;
    height: 163px;
    background: var(--divider);
  }
  .brand-name {
    position: absolute;
    left: 700px;
    top: 126px;
    display: flex;
    align-items: center;
    gap: 14px;
    margin: 0;
    font-size: 30px;
    font-weight: 600;
    letter-spacing: 1px;
    color: var(--text-light);
    white-space: nowrap;
  }
  .brand-name__mark {
    width: 18px;
    height: 18px;
    background: var(--brand-green);
  }
</style>
</head>
<body>
  <section class="signature" aria-label="Email signature">
    <h1 class="person__name">FULL NAME</h1>
    <p class="person__role">CEO | Founder</p>
    <div class="person__rule"></div>

    <ul class="contact-list">
      <li class="contact-list__item">
        <svg class="contact-list__icon" viewBox="0 0 24 24" aria-hidden="true">
          <path fill="#0f9447" d="M6.6 10.8a15.2 15.2 0 0 0 6.6 6.6l2.2-2.2a1 1 0 0 1 1-.25 11.4 11.4 0 0 0 3.6.57 1 1 0 0 1 1 1V20a1 1 0 0 1-1 1A17 17 0 0 1 3 4a1 1 0 0 1 1-1h3.5a1 1 0 0 1 1 1c0 1.25.2 2.45.57 3.6a1 1 0 0 1-.25 1z"/>
        </svg>
        555-210-7384
      </li>
      <li class="contact-list__item">
        <svg class="contact-list__icon" viewBox="0 0 24 24" aria-hidden="true">
          <rect x="1" y="5" width="22" height="14" fill="#0f9447"/>
          <path d="M1 5l11 8 11-8M1 19l8-7M23 19l-8-7" fill="none" stroke="#151515" stroke-width="1.5"/>
        </svg>
        info@tlmbespokehomes.com.au
      </li>
      <li class="contact-list__item">
        <svg class="contact-list__icon" viewBox="0 0 24 24" aria-hidden="true">
          <g fill="none" stroke="#0f9447" stroke-width="1.6">
            <circle cx="12" cy="12" r="10.5"/>
            <ellipse cx="12" cy="12" rx="4.5" ry="10.5"/>
            <path d="M1.5 12h21M3.5 6.5h17M3.5 17.5h17M12 1.5v21"/>
          </g>
        </svg>
        www.tlmbespokehomes.com.au
      </li>
    </ul>

    <div class="signature__divider"></div>

    <p class="brand-name"><span class="brand-name__mark"></span>TLM Bespoke Homes</p>

    <div class="signature__band"></div>
  </section>
</body>
</html>
```